Tobias Grünwald and Co stationary design

Name of business:
Tobias Grünwald and Co

Can be written as:
Tobias Grünwald and Co
Tobias Grünwald & Co
tobias grünwald & co

If broken into letters:
TG&Co
tg&co

We are a Railway Safety Training Company
Our focus is on rail safety, Rail Management, Safety Management, Train Control Training, Accident Investigation.

.
Updates

Project Deadline Extended Reason: The original date was set to commence as soon as the logo contest finished. Quillset hub started the project as soon as it was paid. Added Thursday, May 12, 2016

Target Market(s)

Professionals, CEO's and Managing Directors

Industry/Entity Type

Management Consulting

Font styles to use
Sans Serif

Requirements
Must have
• Professional, Sharp, Creative and modern
• Please note that this is for stationary concept which must include
• - business card
• - letterhead
• - envelope
• - with compliments slip
• - document cover (like book or folder cover)
• - dividers for folders....
• These must all have a common theme or style
Nice to have
• Keep if fresh
Should not have
• Please don't sent just fonts.... Must be creative

```html
<!DOCTYPE html>
<html lang="en">
<head>
<meta charset="utf-8">
<title>Tobias Grünwald &amp; Co — Stationery</title>
<link rel="stylesheet" href="https://fonts.googleapis.com/css2?family=Exo+2:ital,wght@0,700;1,700&family=Roboto:wght@400;500&display=swap">
<style>
:root{
  --blue:#0d4a9c;
  --orange:#f6a623;
  --grey:#e6e6e6;
  --grey-dark:#d4d4d4;
  --white:#ffffff;
  --text:#1d3f7a;
  --backdrop:#ede7df;
}
*{box-sizing:border-box;margin:0;padding:0}
html,body{width:800px;height:1200px;overflow:hidden;background:var(--backdrop)}
body{position:relative;font-family:"Roboto",sans-serif;color:var(--text)}
.piece{position:absolute;background:var(--white);overflow:hidden;box-shadow:0 2px 6px rgba(0,0,0,.18)}
.piece svg.shapes{position:absolute;inset:0;width:100%;height:100%}
.brand{font-family:"Exo 2",sans-serif;font-weight:700;color:var(--blue);white-space:nowrap;display:flex;align-items:center;gap:5px}
.brand .dot{display:inline-block;border-radius:50%;background:var(--orange)}
.brand-white{color:var(--white)}
.tag{font-family:"Exo 2",sans-serif;font-style:italic;font-weight:700;color:var(--white);position:absolute;white-space:nowrap}
.contact{position:absolute;font-size:5.2px;line-height:1.4;color:var(--text);white-space:nowrap}

/* letterhead */
.letterhead{left:38px;top:36px;width:340px;height:440px}
.letterhead .brand{position:absolute;left:10px;top:14px;font-size:8px}
.letterhead .contact{left:0;right:0;bottom:12px;text-align:center}

/* envelope */
.envelope{left:400px;top:36px;width:379px;height:164px}
.envelope .tag{left:0;right:0;top:26px;text-align:center;font-size:9px}

/* compliments slip */
.slip{left:400px;top:216px;width:379px;height:164px}
.slip .brand{position:absolute;left:22px;top:62px;font-size:9px}
.slip .contact{right:12px;bottom:14px;text-align:right}
.slip .contact b{font-family:"Exo 2",sans-serif;font-style:italic;font-size:6px;color:var(--blue)}

/* business card */
.card-front{left:434px;top:395px;width:141px;height:81px}
.card-front .brand{position:absolute;left:5px;top:34px;font-size:5px}
.card-front .name-bar{position:absolute;left:58px;top:10px;width:79px;height:8px;border-radius:4px;background:var(--blue);color:var(--white);font-size:5.5px;text-align:center;line-height:8px}
.card-front .role{position:absolute;left:58px;top:21px;font-size:3.2px;line-height:1.35;color:#555}
.card-front .line{position:absolute;left:58px;width:79px;display:flex;align-items:center;gap:3px;font-size:3.4px;color:#555;border-bottom:.5px solid var(--orange);padding-bottom:2px}
.card-front .line svg{width:5px;height:5px;flex:none}
.card-back{left:434px;top:490px;width:141px;height:81px}
.card-back .tag{left:8px;bottom:12px;font-size:7px}
.card-back .role-top{position:absolute;right:6px;top:6px;font-size:3.3px;font-style:italic;font-weight:500;color:var(--white)}

/* id badge */
.badge{left:604px;top:395px;width:141px;height:187px}
.badge .brand{position:absolute;left:0;right:0;top:42px;justify-content:center;font-size:7px}
.badge .photo{position:absolute;left:45px;top:70px;width:50px;height:62px;background:linear-gradient(#e4e4e4,#9b9b9b)}
.badge .name-bar{position:absolute;left:20px;top:138px;width:101px;height:10px;border-radius:5px;background:var(--blue);color:var(--white);font-size:7px;text-align:center;line-height:10px}
.badge .role{position:absolute;left:0;right:0;top:152px;text-align:center;font-size:5px;line-height:1.45;color:var(--blue)}
.badge .foot{position:absolute;left:0;right:0;bottom:0;height:6px;background:var(--orange)}

/* pens */
.pen{position:absolute;left:84px;width:234px;height:14px;border-radius:7px 10px 10px 7px;display:flex;align-items:center;padding-left:34px;box-shadow:0 2px 3px rgba(0,0,0,.2)}
.pen::after{content:"";position:absolute;right:-8px;top:5px;width:10px;height:4px;background:#999;border-radius:0 2px 2px 0}
.pen span{font-family:"Exo 2",sans-serif;font-style:italic;font-weight:700;font-size:8px;color:var(--white)}
.pen-blue{top:524px;background:var(--blue)}
.pen-orange{top:579px;background:var(--orange)}

/* folders */
.folder-tab{position:absolute;top:618px;height:60px;background:var(--orange)}
.tab-left{left:20px;width:328px;clip-path:polygon(0 95%,100% 0,100% 100%,0 100%)}
.tab-right{left:452px;width:328px;border-radius:30px 0 0 0}
.folder{top:664px;width:360px;height:478px;border-radius:0 28px 0 0}
.folder-left{left:20px}
.folder-right{left:420px}
.folder-left .brand{position:absolute;left:0;right:0;top:150px;justify-content:center;font-size:21px}
.folder-left .tag{left:60px;top:436px;font-size:11px}
.folder-right .brand{position:absolute;left:22px;top:390px;font-size:7.5px}
.folder-right .contact{left:22px;top:412px;color:var(--white);font-size:5.6px}
</style>
</head>
<body>

<section class="piece letterhead">
  <svg class="shapes" viewBox="0 0 340 440" preserveAspectRatio="none">
    <polygon points="200,0 340,0 340,60" fill="var(--grey)"/>
    <polygon points="0,70 70,110 0,160" fill="var(--grey)"/>
    <polygon points="0,110 250,0 330,0 60,130" fill="#f2f2f2"/>
    <polygon points="0,300 40,240 0,340" fill="#f1f1f1"/>
  </svg>
  <div class="brand"><span class="dot" style="width:9px;height:9px"></span>Tobias Grünwald &amp; Co</div>
  <p class="contact">Training and Development Consultant<br>GradDipLLN [Practice], GradDipMGT [Learning], BA [Trng&amp;Dev], ILPF, FBILD.<br>[E] t.grunwald@railmail.net &nbsp;|&nbsp; [M] 0400 555 127 &nbsp;|&nbsp; [A] P.O. Box 412, Westbrook WA 6021</p>
</section>

<section class="piece envelope">
  <svg class="shapes" viewBox="0 0 379 164" preserveAspectRatio="none">
    <polygon points="200,80 300,130 330,100 379,164 260,164" fill="var(--grey)"/>
    <path d="M0 0 H379 L368 56 Q366 64 356 64 H24 Q14 64 12 56 Z" fill="var(--blue)"/>
  </svg>
  <p class="tag">Tobias Grünwald &amp; Co</p>
</section>

<section class="piece slip">
  <svg class="shapes" viewBox="0 0 379 164" preserveAspectRatio="none">
    <polygon points="0,110 379,0 379,15 40,150" fill="#f0f0f0"/>
    <polygon points="290,0 379,0 300,70" fill="var(--grey)"/>
    <polygon points="60,120 120,105 110,150" fill="var(--grey)"/>
  </svg>
  <div class="brand"><span class="dot" style="width:10px;height:10px"></span>Tobias Grünwald &amp; Co</div>
  <p class="contact"><b>Tobias Grünwald &amp; Co</b><br>Training and Development Consultant<br>GradDipLLN [Practice], GradDipMGT [Learning], BA [Trng&amp;Dev], ILPF, FBILD.<br>[E] t.grunwald@railmail.net &nbsp;|&nbsp; [M] 0400 555 127 &nbsp;|&nbsp; [A] P.O. Box 412, Westbrook WA 6021</p>
</section>

<section class="piece card-front">
  <svg class="shapes" viewBox="0 0 141 81" preserveAspectRatio="none">
    <polygon points="0,0 40,0 0,30" fill="#f0f0f0"/>
    <polygon points="110,81 141,50 141,81" fill="var(--grey)"/>
  </svg>
  <div class="brand"><span class="dot" style="width:6px;height:6px"></span>Tobias Grünwald &amp; Co</div>
  <div class="name-bar">Tobias Grünwald</div>
  <p class="role">Director – Training and Development Consultant<br>GradDipLLN [Practice], GradDipMGT [Learning],<br>BA [Trng&amp;Dev], ILPF, FBILD.</p>
  <div class="line" style="top:42px"><svg viewBox="0 0 10 10"><rect x="1" y="2" width="8" height="6" fill="var(--blue)"/></svg>t.grunwald@railmail.net</div>
  <div class="line" style="top:53px"><svg viewBox="0 0 10 10"><rect x="3" y="1" width="4" height="8" rx="1" fill="var(--blue)"/></svg>0400 555 127</div>
  <div class="line" style="top:64px;border:none"><svg viewBox="0 0 10 10"><path d="M5 9 L2 5 A3 3 0 1 1 8 5 Z" fill="var(--blue)"/></svg>P.O. Box 412, Westbrook WA 6021</div>
</section>

<section class="piece card-back">
  <svg class="shapes" viewBox="0 0 141 81" preserveAspectRatio="none">
    <rect width="141" height="81" fill="var(--blue)"/>
    <polygon points="0,0 141,0 141,15 60,15 30,0" fill="var(--blue)"/>
    <polygon points="0,0 60,0 90,40 141,60 141,75 70,45 0,20" fill="var(--grey)"/>
    <polygon points="90,40 120,25 141,60" fill="#f4f4f4"/>
  </svg>
  <p class="role-top">[TRAINING AND DEVELOPMENT CONSULTANT]</p>
  <p class="tag">Tobias Grünwald &amp; Co</p>
</section>

<section class="piece badge">
  <svg class="shapes" viewBox="0 0 141 187" preserveAspectRatio="none">
    <rect width="141" height="110" fill="var(--blue)"/>
    <polygon points="0,100 141,80 141,187 0,187" fill="var(--white)"/>
    <polygon points="0,100 30,110 0,140" fill="var(--grey)"/>
    <polygon points="141,80 110,100 141,130" fill="var(--grey)"/>
  </svg>
  <div class="brand brand-white"><span class="dot" style="width:8px;height:8px"></span>Tobias Grünwald &amp; Co</div>
  <div class="photo" role="img" aria-label="Portrait photograph of the director"></div>
  <div class="name-bar">Tobias Grünwald</div>
  <p class="role">Director – Training and Development Consultant<br>GradDipLLN [Practice], GradDipMGT [Learning],<br>BA [Trng&amp;Dev], ILPF, FBILD.</p>
  <div class="foot"></div>
</section>

<div class="pen pen-blue"><span>Tobias Grünwald &amp; Co</span></div>
<div class="pen pen-orange"><span>Tobias Grünwald &amp; Co</span></div>

<div class="folder-tab tab-left"></div>
<div class="folder-tab tab-right"></div>

<section class="piece folder folder-left">
  <svg class="shapes" viewBox="0 0 360 478" preserveAspectRatio="none">
    <polygon points="0,350 90,290 240,210 360,180 360,276 300,260 100,404 0,404" fill="var(--grey)"/>
    <polygon points="240,210 290,260 360,230 360,180" fill="var(--grey-dark)"/>
    <polygon points="0,300 40,330 0,380" fill="#dedede"/>
    <polygon points="360,276 300,260 100,404 0,404 0,478 360,478" fill="var(--blue)"/>
  </svg>
  <div class="brand"><span class="dot" style="width:22px;height:22px"></span>Tobias Grünwald &amp; Co</div>
  <p class="tag">We are a Railway Safety Training Company</p>
</section>

<section class="piece folder folder-right">
  <svg class="shapes" viewBox="0 0 360 478" preserveAspectRatio="none">
    <polygon points="0,180 120,210 360,300 360,340 60,260 0,276" fill="var(--grey)"/>
    <polygon points="0,180 30,240 0,276" fill="var(--grey-dark)"/>
    <polygon points="300,300 360,260 360,340" fill="var(--grey-dark)"/>
    <polygon points="0,276 60,260 360,432 360,478 0,478" fill="var(--blue)"/>
  </svg>
  <div class="brand brand-white"><span class="dot" style="width:9px;height:9px"></span>Tobias Grünwald &amp; Co</div>
  <p class="contact">Training and Development Consultant<br>GradDipLLN [Practice], GradDipMGT [Learning], BA [Trng&amp;Dev], ILPF, FBILD.<br>[E] t.grunwald@railmail.net &nbsp;|&nbsp; [M] 0400 555 127 &nbsp;|&nbsp; [A] P.O. Box 412, Westbrook WA 6021</p>
</section>

</body>
</html>
```